Stationery Design Project

We need letterhead and business cards designed for our consulting firm. Color scheme, mostly deep blue (see logo). We are a commercial consulting work out firm, nationwide (large loans, $10MM and up). Visit our website for more info.
Updates

Project Deadline Extended
Reason: Meeting tomorrow morning to make final final decision. Would like this project to stay open to be able to provide feed back and receive final edits and approve. Thank you!!!

Target Market(s)

High end investors

Industry/Entity Type

Business

Requirements
Must have
• Letterhead must have the logo and the address

4719 Harlow Court, Suite 210, San Diego, CA 92108
Nice to have
• It would be nice to incorporate a watermark of all or some portion of the logo on the letterhead, or at least for the 2nd sheets.

Maybe our phone number: 858.555.0172
and/or webiste: www.tallpinecapital-example.com
Should not have
• Target users and audience of this will be men so, frilly or whimsical type designs are not preferred.

```html
<!DOCTYPE html>
<html lang="en">
<head>
<meta charset="utf-8">
<title>Tallpine Capital Partners – Business Cards</title>
<link href="https://fonts.googleapis.com/css2?family=Crimson+Text:wght@400;600&display=swap" rel="stylesheet">
<style>
  :root {
    --page-bg: #f1f1f2;
    --blue-deep: #0f4a8e;
    --blue-mid: #1e6fb6;
    --blue-light: #3a9bd6;
    --band-blue: #1f5aa3;
    --band-blue-end: #4a78ab;
    --gray-light: #a9acb0;
    --gray-dark: #5a5e64;
    --name-gray: #7d7f82;
    --white: #ffffff;
    --shadow: rgba(0, 0, 0, 0.28);
  }
  * { box-sizing: border-box; margin: 0; padding: 0; }
  html, body {
    width: 1200px;
    height: 905px;
    overflow: hidden;
    background: var(--page-bg);
    font-family: "Crimson Text", Georgia, serif;
  }
  .stage { position: relative; width: 1200px; height: 905px; }

  .card {
    position: absolute;
    width: 600px;
    height: 343px;
    box-shadow: 0 14px 30px var(--shadow);
    overflow: hidden;
  }

  /* Front */
  .card--front {
    left: 120px;
    top: 110px;
    background: radial-gradient(ellipse at 45% 40%, var(--blue-light) 0%, var(--blue-mid) 45%, var(--blue-deep) 100%);
    color: var(--white);
    text-align: center;
  }
  .card--front .brand-name {
    position: absolute;
    left: 0; right: 0;
    top: 120px;
    font-size: 40px;
    font-weight: 400;
    letter-spacing: 2px;
    text-transform: uppercase;
  }
  .card--front .website {
    position: absolute;
    left: 0; right: 0;
    bottom: 60px;
    font-size: 17px;
    letter-spacing: 1.5px;
    text-transform: uppercase;
  }

  /* Back */
  .card--back {
    left: 480px;
    top: 450px;
    background: linear-gradient(160deg, #ffffff 0%, #f4f4f5 60%, #e6e7e8 100%);
  }
  .card--back .brand-name {
    position: absolute;
    left: 230px;
    right: 20px;
    top: 40px;
    text-align: center;
    color: var(--name-gray);
    font-size: 34px;
    font-weight: 400;
    letter-spacing: 2px;
    text-transform: uppercase;
  }
  .holder-band {
    position: absolute;
    left: 0;
    top: 140px;
    width: 300px;
    height: 90px;
    background: linear-gradient(90deg, var(--band-blue), var(--band-blue-end));
    color: var(--white);
    padding: 14px 0 0 36px;
  }
  .holder-band .holder-name { font-size: 26px; font-weight: 600; line-height: 1.1; }
  .holder-band .holder-title { font-size: 19px; font-weight: 600; margin-left: 14px; }

  .contact-band {
    position: absolute;
    left: 300px;
    top: 185px;
    width: 300px;
    height: 120px;
    background: linear-gradient(90deg, var(--gray-light), var(--gray-dark));
    color: var(--white);
    text-align: right;
    padding: 10px 18px 0 10px;
    font-size: 14px;
    font-weight: 600;
    line-height: 1.3;
  }
  .contact-band .phones span + span { margin-left: 12px; }
</style>
</head>
<body>
<main class="stage">
  <section class="card card--front">
    <p class="brand-name">Tallpine Capital Partners</p>
    <p class="website">www.tallpinecapital-example.com</p>
  </section>

  <section class="card card--back">
    <p class="brand-name">Tallpine Capital Partners</p>
    <div class="holder-band">
      <p class="holder-name">Daniel Mercer</p>
      <p class="holder-title">Founder / Owner</p>
    </div>
    <address class="contact-band" style="font-style:normal">
      <p>4719 Harlow Court, Suite 210,</p>
      <p>San Diego, CA 92108</p>
      <p class="phones"><span>T. 858.555.0172</span><span>F. 858.555.0189</span></p>
      <p>E: info@tallpinecapital-example.com</p>
    </address>
  </section>
</main>
</body>
</html>
```